Post Card Design - Photo on front, details on back. Logo on both sides.

Back: See the photo of my old card. The back worked well, as it gave me lots of space to write on. The address details are still correct, but the logo has changed to Josephine Sans. Logo can be on one line or on two (if two, align it on the left).
Don't include the 'BEAUTIFUL WEDDING DRESSES...' bit.
I'd like to print this on thicker, slightly coarse paper, so don't go too small on detail.
Here are the Plume paper details: Paper Stock: Natural Uncoated
Paper Thickness: Premium
Finish: None
Front of Card: I'd like to see options for both pictures:
I think the painted image would look best with a frame in a pale shade and the logo in the frame fairly subtle.
The actual dress photo I'd like to see cropped a bit like in my mock up. You'll need to have a look at how the logo would be best placed on this. You can place it anywhere, or add a banner.
See my website for my brand's look: vistaplume.co.nz
Target Market(s)
Brides
Industry/Entity Type
Wedding Dresses
Contact Information for Business Card
Front: Photo and logo. Back: with details and lots of empty space. See attached photos for loose brief.
Other font styles liked:
- Josephine Sans
Requirements
Must have
- I hand-write the gown designs and price on the back of the card, so there needs to be plenty of empty space.
Nice to have
- As per brief.
Should not have
- It must look clean, romantic, modern. Timeless.

```html
<!DOCTYPE html>
<html lang="en">
<head>
<meta charset="utf-8">
<title>Vista Plume – Post Card</title>
<link href="https://fonts.googleapis.com/css2?family=Josefin+Sans:wght@300;400&family=Montserrat:wght@700&display=swap" rel="stylesheet">
<style>
  :root {
    --page: #ffffff;
    --ink-light: #fbf7f2;
    --photo-warm-deep: #b98a5c;
    --photo-warm-mid: #dcc09c;
    --photo-warm-pale: #f3e6d4;
    --photo-dress: #f7f2ec;
    --wash-pale: #f6ede2;
    --wash-mid: #e9d8c2;
  }
  * { margin: 0; padding: 0; box-sizing: border-box; }
  html, body {
    width: 1200px; height: 1200px; overflow: hidden;
    background: var(--page);
  }
  .canvas { position: relative; width: 1200px; height: 1200px; }

  .card {
    position: absolute; width: 400px; height: 719px; overflow: hidden;
  }
  .card--front { left: 182px; top: 241px; }
  .card--back  { left: 618px; top: 239px; }

  .card__photo { position: absolute; inset: 0; }
  .card--front .card__photo {
    background:
      radial-gradient(ellipse 40% 55% at 100% 75%, var(--photo-dress) 0%, rgba(247,242,236,0.6) 45%, transparent 75%),
      linear-gradient(180deg, transparent 0%, transparent 66%, rgba(156,117,96,0.55) 82%, rgba(140,100,80,0.7) 100%),
      linear-gradient(90deg, var(--photo-warm-deep) 0%, var(--photo-warm-mid) 30%, var(--photo-warm-pale) 70%, #f0dfc6 100%);
  }
  .card--back .card__photo {
    background:
      radial-gradient(ellipse 40% 55% at 0% 75%, #fbf8f4 0%, rgba(251,248,244,0.6) 45%, transparent 75%),
      linear-gradient(180deg, transparent 0%, transparent 66%, rgba(199,171,152,0.5) 84%, rgba(185,160,150,0.6) 100%),
      linear-gradient(90deg, var(--wash-pale) 0%, var(--wash-mid) 45%, var(--wash-pale) 75%, var(--wash-mid) 100%);
  }

  .brand {
    position: absolute;
    font-family: "Josefin Sans", sans-serif;
    font-weight: 300;
    color: var(--ink-light);
    text-transform: uppercase;
    letter-spacing: 0.04em;
    white-space: nowrap;
  }
  .card--front .brand { left: 113px; top: 289px; font-size: 42px; line-height: 49px; }
  .card--back .brand  { left: 48px;  top: 68px;  font-size: 28px; line-height: 32px; }
  .brand__line { display: block; }

  .website {
    position: absolute; left: 114px; top: 391px;
    font-family: "Josefin Sans", sans-serif; font-weight: 400;
    font-size: 20px; letter-spacing: 0.02em;
    color: var(--ink-light); white-space: nowrap;
  }
  .phone {
    position: absolute; left: 123px; top: 477px;
    font-family: "Montserrat", sans-serif; font-weight: 700;
    font-size: 29px; letter-spacing: 0.01em;
    color: var(--ink-light); white-space: nowrap;
  }

  .writing-lines {
    position: absolute; left: 32px; top: 0; width: 335px; height: 719px;
  }
  .writing-lines line { stroke: var(--ink-light); stroke-width: 1.5; }
</style>
</head>
<body>
<div class="canvas">

  <section class="card card--front">
    <div class="card__photo" role="img" aria-label="Photograph of a bride from behind in a fitted white gown with a long train, standing in a sunlit sandstone colonnade"></div>
    <div class="brand">
      <span class="brand__line">Vista</span>
      <span class="brand__line">Plume</span>
    </div>
    <p class="website">vistaplume.co.nz</p>
    <p class="phone">XXX-XXX-XX</p>
  </section>

  <section class="card card--back">
    <div class="card__photo" role="img" aria-label="Pale washed-out version of the bridal gown photograph in the sandstone colonnade"></div>
    <div class="brand">
      <span class="brand__line">Vista</span>
      <span class="brand__line">Plume</span>
    </div>
    <svg class="writing-lines" viewBox="0 0 335 719" aria-hidden="true">
      <line x1="0" y1="188" x2="335" y2="188"/>
      <line x1="0" y1="249" x2="335" y2="249"/>
      <line x1="0" y1="310" x2="335" y2="310"/>
      <line x1="0" y1="371" x2="335" y2="371"/>
      <line x1="0" y1="432" x2="335" y2="432"/>
      <line x1="0" y1="493" x2="335" y2="493"/>
    </svg>
  </section>

</div>
</body>
</html>
```